Monthly Planner & To Do List on dry erase magnetic whiteboard

I'm after 2 x designs for magnetic whiteboards.
1. 17 x 13 inches is a monthly planner. Dates and month can be written in each month and then wiped off and re-written for the next month.
2. 6 x 4 inches - to do list however I don't want this to say To Do on it but will have lines to write on and possibly bullet points to check off.
I have attached below samples of other products (the ones I like the most are the first two - 9.19.52 and 9.20.34). I actually don't like the design of the others but just show them here as an example for layout purposes.
I want something that is modern, slick, simple yet stylish which is what my brand is representative of - smart, modern, organised. It will be printed onto a white board and I only want the print to be in black, no grey shading. I need a more modern font and don't like any of the swirly parts. Just clean and simple but slick.
I would like the size of the day squares to be as large as possible to fit writing in them and also for a section somewhere on the page for additional notes.

Requirements
Should not have
• Old style fonts, cartoon style or childish.

```html
<!DOCTYPE html>
<html lang="en">
<head>
<meta charset="utf-8">
<title>Monthly Planner</title>
<link rel="stylesheet" href="https://fonts.googleapis.com/css2?family=Comfortaa:wght@400;500&display=swap">
<style>
  :root {
    --ink: #000000;
    --board: #ffffff;
  }
  html, body {
    margin: 0;
    padding: 0;
    width: 1200px;
    height: 918px;
    overflow: hidden;
    background: var(--board);
  }
  .planner {
    display: block;
    width: 1200px;
    height: 918px;
  }
  .planner text {
    font-family: "Comfortaa", sans-serif;
    fill: var(--ink);
  }
  .planner__title { font-size: 33px; }
  .month-tab__label { font-size: 17px; }
  .day-label, .notes-label { font-size: 24px; }
  .month-tab__outline {
    fill: none;
    stroke: var(--ink);
    stroke-width: 1;
    stroke-dasharray: 3 3;
  }
  .grid-line {
    stroke: var(--ink);
    stroke-width: 2;
    fill: none;
  }
</style>
</head>
<body>
<svg class="planner" viewBox="0 0 1224 936" preserveAspectRatio="none" xmlns="http://www.w3.org/2000/svg">
  <text class="planner__title" x="18" y="72">month</text>

  <g class="month-tabs">
    <path class="month-tab__outline" d="M180 0V68A28 28 0 0 0 236 68V0"/>
    <path class="month-tab__outline" d="M267 0V68A28 28 0 0 0 323 68V0"/>
    <path class="month-tab__outline" d="M355 0V68A28 28 0 0 0 411 68V0"/>
    <path class="month-tab__outline" d="M443 0V68A28 28 0 0 0 499 68V0"/>
    <path class="month-tab__outline" d="M530 0V68A28 28 0 0 0 586 68V0"/>
    <path class="month-tab__outline" d="M618 0V68A28 28 0 0 0 674 68V0"/>
    <path class="month-tab__outline" d="M706 0V68A28 28 0 0 0 762 68V0"/>
    <path class="month-tab__outline" d="M793 0V68A28 28 0 0 0 849 68V0"/>
    <path class="month-tab__outline" d="M882 0V68A28 28 0 0 0 938 68V0"/>
    <path class="month-tab__outline" d="M969 0V68A28 28 0 0 0 1025 68V0"/>
    <path class="month-tab__outline" d="M1057 0V68A28 28 0 0 0 1113 68V0"/>
    <path class="month-tab__outline" d="M1144 0V68A28 28 0 0 0 1200 68V0"/>
    <g text-anchor="middle">
      <text class="month-tab__label" x="208" y="28">jan</text>
      <text class="month-tab__label" x="295" y="28">feb</text>
      <text class="month-tab__label" x="383" y="28">mar</text>
      <text class="month-tab__label" x="471" y="28">apr</text>
      <text class="month-tab__label" x="558" y="28">may</text>
      <text class="month-tab__label" x="646" y="28">jun</text>
      <text class="month-tab__label" x="734" y="28">july</text>
      <text class="month-tab__label" x="820" y="28">aug</text>
      <text class="month-tab__label" x="910" y="28">sep</text>
      <text class="month-tab__label" x="997" y="28">oct</text>
      <text class="month-tab__label" x="1085" y="28">nov</text>
      <text class="month-tab__label" x="1172" y="28">dec</text>
    </g>
  </g>

  <g class="calendar-grid">
    <path class="grid-line" d="
      M0 121H136 M149 121H277 M290 121H419 M433 121H562 M576 121H705 M718 121H847 M863 121H992 M1003 121H1224
      M0 284H136 M149 284H277 M290 284H419 M433 284H562 M576 284H705 M718 284H847 M863 284H997
      M0 447H136 M149 447H277 M290 447H419 M433 447H562 M576 447H705 M718 447H847 M863 447H997
      M0 610H136 M149 610H277 M290 610H419 M433 610H562 M576 610H705 M718 610H847 M863 610H997
      M0 773H136 M149 773H277 M290 773H419 M433 773H562 M576 773H705 M718 773H847 M863 773H997"/>
    <path class="grid-line" d="
      M142 131V277 M142 289V440 M142 453V603 M142 616V765 M142 779V930
      M285 131V277 M285 289V440 M285 453V603 M285 616V765 M285 779V930
      M428 131V277 M428 289V440 M428 453V603 M428 616V765 M428 779V930
      M570 131V277 M570 289V440 M570 453V603 M570 616V765 M570 779V930
      M712 131V277 M712 289V440 M712 453V603 M712 616V765 M712 779V930
      M855 131V277 M855 289V440 M855 453V603 M855 616V765 M855 779V930
      M997 131V930"/>
  </g>

  <g class="day-labels">
    <text class="day-label" x="14" y="155">sun</text>
    <text class="day-label" x="157" y="155">mon</text>
    <text class="day-label" x="295" y="155">tue</text>
    <text class="day-label" x="439" y="155">wed</text>
    <text class="day-label" x="581" y="155">thu</text>
    <text class="day-label" x="727" y="155">fri</text>
    <text class="day-label" x="866" y="155">sat</text>
  </g>
  <text class="notes-label" x="1070" y="155">notes</text>
</svg>
</body>
</html>
```